Whitmore Properties
business cards, stationery
Can you please extend the contest ....
can you please extend the contest?
@vElpo - we like the black and gold card in #16 but do not like the gold and white stationary. We would like more black in the stationary with gold being the accent with more focus at the top of the stationary.
The font used in our logo is "Trajanpro" both regular and bold.
kindly tell the font name which is used in your logo ...

```html
<!DOCTYPE html>
<html lang="en">
<head>
<meta charset="utf-8">
<title>Whitmore Properties – Stationery</title>
<link rel="stylesheet" href="https://fonts.googleapis.com/css2?family=Cinzel:wght@600&family=Open+Sans:wght@400;600&display=swap">
<style>
:root{
  --bg:#e4e4e2;
  --black:#121212;
  --charcoal:#2c2c2c;
  --gold:#f39a1e;
  --gold-deep:#e07b0c;
  --gold-light:#fbc069;
  --grey:#a9a9a9;
  --grey-light:#d6d6d6;
  --white:#ffffff;
  --ink:#333333;
  --muted:#cfcfcf;
}
*{box-sizing:border-box;margin:0;padding:0}
html,body{width:1200px;height:802px;overflow:hidden;background:var(--bg)}
body{position:relative;font-family:"Open Sans",Arial,sans-serif;color:var(--ink)}
.piece{position:absolute;overflow:hidden;box-shadow:0 3px 10px rgba(0,0,0,.25)}
.swoosh{position:absolute;left:0;bottom:0;width:100%;display:block}
.brand{display:flex;align-items:center;gap:8px;font-family:"Cinzel",serif;font-weight:600;letter-spacing:.06em;line-height:1.05;color:var(--white)}
.brand-mark{display:block;flex:none;background:var(--gold)}
.brand-text{display:block}

/* business card fronts */
.card-front{width:222px;height:146px;top:34px;background:linear-gradient(180deg,var(--charcoal) 0%,var(--black) 60%)}
.card-front .contact{position:absolute;left:12px;top:12px;font-size:5.5px;line-height:1.6;color:var(--muted)}
.card-front .brand{position:absolute;right:12px;top:40px;font-size:11px;gap:6px}
.card-front .brand-mark{width:12px;height:12px}
.card-front .holder{position:absolute;left:14px;top:114px;font-size:7px;line-height:1;font-weight:600;color:var(--black)}

/* business card backs */
.card-back{width:222px;height:146px;top:190px;display:flex;align-items:center;justify-content:center}
.card-back.gold{background:radial-gradient(circle at 50% 45%,var(--gold-light),var(--gold-deep))}
.card-back.grey{background:radial-gradient(circle at 50% 45%,var(--grey-light),var(--grey))}
.card-back .square{width:40px;height:40px;background:rgba(255,255,255,.22)}

/* envelopes */
.envelope{left:72px;width:564px;background:var(--white)}
.envelope.back{top:370px;height:170px;background:linear-gradient(180deg,#f2f2f2,#dcdcdc)}
.envelope.back svg{position:absolute;left:0;top:0;width:100%;height:100%}
.envelope.front{top:556px;height:188px}
.envelope .header{position:absolute;left:0;top:0;width:100%;height:62px;background:var(--black)}
.envelope .header::after{content:"";position:absolute;left:0;bottom:-4px;width:100%;height:4px;background:var(--gold)}
.envelope .brand{position:absolute;left:22px;top:13px;font-size:16px}
.envelope .brand-mark{width:18px;height:18px}
.envelope .return{position:absolute;right:22px;top:17px;font-size:6.5px;line-height:1.6;color:var(--muted);text-align:right}

/* letterhead */
.letterhead{left:660px;top:110px;width:468px;height:634px;background:var(--white)}
.letterhead .header{position:absolute;left:0;top:0;width:100%;height:118px;background:linear-gradient(180deg,var(--charcoal),var(--black))}
.letterhead .accent{position:absolute;left:0;top:118px;width:100%;height:22px;display:block}
.letterhead .brand{position:absolute;left:30px;top:38px;font-size:20px}
.letterhead .brand-mark{width:22px;height:22px}
.letterhead .header-contact{position:absolute;right:30px;top:40px;font-size:6.5px;line-height:1.7;color:var(--muted);text-align:right}
.letterhead .footer{position:absolute;left:0;bottom:0;width:100%;height:26px;background:var(--black);border-top:3px solid var(--gold)}
.letterhead .footer-text{position:absolute;left:30px;top:7px;font-size:6.5px;color:var(--muted);letter-spacing:.04em}
</style>
</head>
<body>

<!-- business card front: gold -->
<section class="piece card-front" style="left:67px">
  <p class="contact">218 Alder Crest Way<br>Ridgefield, Oregon 97321<br>(555) 214-7730<br>dana@whitmoreproperties.com</p>
  <div class="brand"><span class="brand-mark"></span><span class="brand-text">WHITMORE</span></div>
  <svg class="swoosh" viewBox="0 0 222 50" height="50" preserveAspectRatio="none">
    <path d="M0 4 Q120 34 222 0 L222 50 L0 50Z" fill="var(--white)"/>
    <path d="M0 30 Q130 40 222 16 L222 50 L0 50Z" fill="var(--gold)"/>
  </svg>
  <p class="holder">Dana Holloway</p>
</section>

<!-- business card front: grey -->
<section class="piece card-front" style="left:324px">
  <p class="contact">218 Alder Crest Way<br>Ridgefield, Oregon 97321<br>(555) 214-7730<br>dana@whitmoreproperties.com</p>
  <div class="brand"><span class="brand-mark"></span><span class="brand-text">WHITMORE</span></div>
  <svg class="swoosh" viewBox="0 0 222 50" height="50" preserveAspectRatio="none">
    <path d="M0 4 Q120 34 222 0 L222 50 L0 50Z" fill="var(--white)"/>
    <path d="M0 30 Q130 40 222 16 L222 50 L0 50Z" fill="var(--grey)"/>
  </svg>
  <p class="holder">Dana Holloway</p>
</section>

<!-- business card backs -->
<section class="piece card-back gold" style="left:67px"><span class="square"></span></section>
<section class="piece card-back grey" style="left:324px"><span class="square"></span></section>

<!-- envelope back with black flap and gold edge -->
<section class="piece envelope back">
  <svg viewBox="0 0 564 170" preserveAspectRatio="none">
    <path d="M0 0 L564 0 L564 70 Q430 20 282 60 Q130 100 0 60Z" fill="var(--black)"/>
    <path d="M0 60 Q130 100 282 60 Q430 20 564 70 L564 77 Q430 28 282 68 Q130 108 0 68Z" fill="var(--gold)"/>
  </svg>
</section>

<!-- envelope front -->
<section class="piece envelope front">
  <div class="header">
    <div class="brand"><span class="brand-mark"></span><span class="brand-text">WHITMORE<br>PROPERTIES</span></div>
    <p class="return">218 Alder Crest Way<br>Ridgefield, Oregon 97321</p>
  </div>
</section>

<!-- letterhead -->
<section class="piece letterhead">
  <div class="header">
    <div class="brand"><span class="brand-mark"></span><span class="brand-text">WHITMORE<br>PROPERTIES</span></div>
    <p class="header-contact">218 Alder Crest Way<br>Ridgefield, Oregon 97321<br>(555) 214-7730<br>dana@whitmoreproperties.com</p>
  </div>
  <svg class="accent" viewBox="0 0 468 22" preserveAspectRatio="none">
    <path d="M0 0 L468 0 L468 6 Q240 22 0 4Z" fill="var(--gold)"/>
  </svg>
  <div class="footer"><p class="footer-text">www.whitmoreproperties.com</p></div>
</section>

</body>
</html>
```